Quorvantelline.com

I need a site that I can sell dewatering equipment to the construction industry.
Ie, pipes fittings pumps and other such things needed to remove the groundwater on construction sites. Here in Florida, it’s needed almost everywhere seeing we are at sea level.
I want to be able to sell these products on the site and receive

Coded - Design and coding required

1 page

```html
<!DOCTYPE html>
<html lang="en">
<head>
<meta charset="utf-8">
<title>Quorvantelline.com – Dewatering Equipment</title>
<link rel="stylesheet" href="https://fonts.googleapis.com/css2?family=Oswald:wght@300;400;500&family=Lato:wght@400;700&family=Montserrat:wght@500;600;700&display=swap">
<style>
  :root{
    --brand-blue:#1f74c9;
    --cta-blue:#1a8fd0;
    --navy:#0e3f8f;
    --band-blue:#2357c2;
    --deep-blue:#0d4aa8;
    --ink:#2b2b2b;
    --muted:#5a5a5a;
    --dark:#2d2d2d;
    --topbar:#2a2a2a;
    --paper:#ffffff;
    --grid-bg:#eeeeee;
    --label-dark:#262626;
  }
  *{margin:0;padding:0;box-sizing:border-box}
  html,body{width:1200px;height:3502px;overflow:hidden}
  body{position:relative;background:var(--paper);font-family:'Lato',sans-serif;color:var(--ink)}
  .abs{position:absolute}

  /* top bar */
  .topbar{left:0;top:0;width:1200px;height:38px;background:var(--topbar);color:#fff;font:700 13px 'Montserrat',sans-serif;letter-spacing:.5px}
  .topbar .call{position:absolute;left:117px;top:12px}
  .topbar .social{position:absolute;right:117px;top:12px;display:flex;gap:12px}
  .topbar .social span{width:14px;height:14px;border-radius:50%;background:#8a8a8a;display:block}

  /* nav */
  .nav{left:0;top:38px;width:1200px;height:90px;background:var(--paper)}
  .logo{position:absolute;left:117px;top:30px;display:flex;align-items:center;gap:8px;font:500 25px 'Oswald',sans-serif;color:var(--brand-blue);letter-spacing:.3px;white-space:nowrap}
  .logo i{width:24px;height:24px;border-radius:50%;background:var(--brand-blue);display:block}
  .menu{position:absolute;left:372px;top:38px;width:578px;display:flex;justify-content:space-between;font:500 13px 'Montserrat',sans-serif;color:#222;letter-spacing:.2px;white-space:nowrap}
  .quote-btn{position:absolute;left:972px;top:31px;width:112px;height:34px;background:var(--cta-blue);color:#fff;font:600 11px 'Montserrat',sans-serif;display:flex;align-items:center;justify-content:center;letter-spacing:.4px}

  /* hero */
  .hero{left:0;top:128px;width:1200px;height:654px;background:linear-gradient(180deg,#7e93a8 0%,#9aa4a2 45%,#6d6a4d 72%,#3e4a35 100%);clip-path:polygon(0 0,100% 0,100% 527px,0 654px)}
  .hero-title{left:120px;top:138px;width:960px;text-align:center;color:#fff;font:500 34px/1.22 'Montserrat',sans-serif;text-shadow:0 2px 6px rgba(0,0,0,.5)}
  .hero-btn{left:488px;top:292px;width:224px;height:58px;background:var(--cta-blue);color:#fff;font:700 23px 'Montserrat',sans-serif;display:flex;align-items:center;justify-content:center;letter-spacing:.5px}

  /* welcome */
  .welcome-title{left:117px;top:856px;font:400 32px 'Oswald',sans-serif;color:var(--brand-blue)}
  .welcome-text{left:117px;top:906px;width:520px;font:400 15px/1.45 'Lato',sans-serif;color:var(--muted)}
  .welcome-text p+p{margin-top:22px}
  .welcome-photo{left:690px;top:864px;width:391px;height:252px;background:linear-gradient(135deg,#6f7478,#3d4146 55%,#8a8f93);box-shadow:6px 8px 14px rgba(0,0,0,.35)}

  /* industries */
  .industries{left:0;top:1195px;width:1200px;height:545px;background:linear-gradient(180deg,#2b5fc6,#2351b7)}
  .section-title{width:1200px;left:0;text-align:center;font:400 32px 'Oswald',sans-serif}
  .industries .section-title{top:63px;color:#fff}
  .industry{top:170px;width:220px;color:#fff}
  .industry svg{display:block;width:56px;height:56px;margin-bottom:18px}
  .industry h3{font:400 22px 'Oswald',sans-serif;margin-bottom:4px;white-space:nowrap}
  .industry p{font:400 12.5px/1.45 'Lato',sans-serif;color:#e4ebf9}

  /* pumps */
  .pumps{left:0;top:1740px;width:1200px;height:812px;background-color:var(--grid-bg);background-image:linear-gradient(#dedede 1px,transparent 1px),linear-gradient(90deg,#dedede 1px,transparent 1px);background-size:47px 47px}
  .pumps .section-title{top:48px;color:#1a1a1a}
  .pump-card{width:309px;height:236px;background:#fff;border:1px solid #d4d4d4}
  .pump-photo{position:absolute;left:6px;top:6px;right:6px;bottom:6px}
  .pump-label{position:absolute;right:6px;bottom:6px;width:278px;height:44px;background:var(--label-dark);clip-path:polygon(28px 0,100% 0,100% 100%,0 100%);color:#fff;font:400 19px 'Oswald',sans-serif;display:flex;align-items:center;justify-content:flex-end;padding-right:16px;letter-spacing:.3px;white-space:nowrap}
  .pump-cta{left:0;top:2453px;width:1200px;display:flex;justify-content:center;align-items:center;gap:22px}
  .pump-cta .call{font:700 24px 'Montserrat',sans-serif;color:#111}
  .pump-cta .btn{width:270px;height:64px;background:var(--navy);color:#fff;font:700 23px 'Montserrat',sans-serif;display:flex;align-items:center;justify-content:center;border-radius:3px}

  /* construction dewatering */
  .construction{left:0;top:2552px;width:1200px;height:666px;background:linear-gradient(180deg,#1055b3,#0c4399)}
  .construction .section-title{top:52px;color:#fff}
  .system{top:133px;width:310px;color:#fff}
  .system-photo{height:182px}
  .system-label{height:45px;background:#fff;clip-path:polygon(28px 0,100% 0,100% 100%,0 100%);font:400 19px 'Oswald',sans-serif;color:#222;display:flex;align-items:center;justify-content:center}
  .system p{margin-top:22px;font:400 14px/1.4 'Lato',sans-serif;color:#fff}

  /* footer */
  .footer{left:0;top:3150px;width:1200px;height:352px;background:var(--dark);clip-path:polygon(0 68px,100% 0,100% 100%,0 100%)}
  .footer-name{left:120px;top:3287px;font:700 19px 'Lato',sans-serif;color:#fff}
  .footer-address{left:120px;top:3316px;font:400 14px 'Lato',sans-serif;color:#fff}
  .footer-contact{left:120px;top:3346px;font:400 15px 'Lato',sans-serif;color:#fff;word-spacing:2px}
  .footer-rule{left:117px;top:3414px;width:966px;height:1px;background:#4a4a4a}
  .footer-copy{left:120px;top:3444px;font:400 13px 'Lato',sans-serif;color:#fff}
  .footer-links{right:117px;top:3444px;font:400 13px 'Lato',sans-serif;color:#fff;word-spacing:3px}
  .badge-a{left:930px;top:3296px;width:50px;height:60px;background:#c8ccd6;border-radius:3px}
  .badge-b{left:970px;top:3292px;width:62px;height:62px;border-radius:50%;background:radial-gradient(circle,#e6c76a,#b58a2b)}
</style>
</head>
<body>

<header class="abs topbar">
  <div class="call">CALL US: 555 210 4471</div>
  <div class="social"><span></span><span></span><span></span></div>
</header>

<nav class="abs nav">
  <div class="logo"><i></i>QUORVANTELLINE</div>
  <div class="menu">
    <span>HOME</span><span>INDUSTRY</span><span>PRODUCT</span><span>SERVICES</span><span>RESOURSE</span><span>ABOUT</span><span>CONTACT</span>
  </div>
  <div class="quote-btn">GET A QUOTE</div>
</nav>

<section class="abs hero" role="img" aria-label="Trailer-mounted dewatering pump beside a lake">
  <h1 class="abs hero-title">QUORVANTELLINE OFFERS PRODUCTS AND<br>SERVICES TO MEET A WIDE RANGE OF<br>GROUNDWATER PUMPING APPLICATIONS.</h1>
  <div class="abs hero-btn">MAKE ENQUIRY</div>
</section>

<h2 class="abs welcome-title">WELCOME QUORVANTELLINE</h2>
<div class="abs welcome-text">
  <p>Our team supplies pumps, pipe, fittings and hoses for dewatering on job sites across the state. We stock the parts crews need, ship them fast and stand behind every unit we sell. Call us for advice on sizing a system for your ground.</p>
  <p>We rent and sell complete systems, from a single trash pump to full wellpoint layouts, and our crews can set them up on site when you need help.</p>
</div>
<div class="abs welcome-photo" role="img" aria-label="Portable pump with hose on a paved site"></div>

<section class="abs industries" aria-label="Industries">
  <h2 class="abs section-title">INDUSTRIES</h2>
  <div class="abs industry" style="left:117px">
    <svg viewBox="0 0 56 56" fill="none" stroke="#fff" stroke-width="2.5"><path d="M16 54V8M22 54V8M16 14h34M8 14h8M16 8l6 6M44 14v14M40 28h8v6h-8z"/><path d="M10 54h18"/></svg>
    <h3>CIVIL CONSTRUCTION</h3>
    <p>Keep trenches, footings and basements dry with pumps and wellpoints sized for the job. We supply the gear that lets road, utility and building crews work below the water table.</p>
  </div>
  <div class="abs industry" style="left:367px">
    <svg viewBox="0 0 56 56" fill="#fff"><path d="M28 6L4 26h8v14h32V26h8z"/><rect x="22" y="28" width="12" height="12" fill="#2b5fc6"/><path d="M2 46q7-5 13 0t13 0 13 0 13 0v4q-7-5-13 0t-13 0-13 0-13 0z"/></svg>
    <h3>DISASTER RECOVERY</h3>
    <p>When storms flood streets and homes, fast pumps matter. Our portable units move large volumes of water quickly and can be on site within hours of your call.</p>
  </div>
  <div class="abs industry" style="left:609px">
    <svg viewBox="0 0 56 56" fill="#fff"><path d="M6 52L6 20L50 52z"/><path d="M30 8l12 12-4 4-12-12z"/><rect x="34" y="18" width="3" height="20" transform="rotate(-45 35 28)"/></svg>
    <h3>MINING / QUARRIES</h3>
    <p>Pits and quarries take on water every day. Our heavy duty pumps handle solids and long runs, keeping the face dry and work moving through every shift.</p>
  </div>
  <div class="abs industry" style="left:857px">
    <svg viewBox="0 0 56 56" fill="#fff"><rect x="25" y="6" width="6" height="10"/><rect x="18" y="16" width="20" height="12"/><path d="M6 30h44l-6 14H12z"/><path d="M4 48q6-4 12 0t12 0 12 0 12 0v4q-6-4-12 0t-12 0-12 0-12 0z"/></svg>
    <h3>MARINE</h3>
    <p>Cofferdams, docks and seawalls need steady pumping. We supply systems built for salt air and tidal water along the coast.</p>
  </div>
</section>

<section class="abs pumps" aria-label="Pumps">
  <h2 class="abs section-title">PUMPS</h2>
</section>
<div class="abs pump-card" style="left:117px;top:1882px"><div class="pump-photo" role="img" aria-label="Blue trailer-mounted trash pump" style="background:linear-gradient(135deg,#e9eef3,#3a5a8c 60%,#d9dde2)"></div><div class="pump-label">TRASH SERIES PUMP</div></div>
<div class="abs pump-card" style="left:446px;top:1882px"><div class="pump-photo" role="img" aria-label="Framed centrifugal pump with engine" style="background:linear-gradient(135deg,#f2f2ee,#c9b64a 40%,#4a4a48 70%,#e6e6e6)"></div><div class="pump-label">CENTRIFUGAL DEWATERING</div></div>
<div class="abs pump-card" style="left:775px;top:1882px"><div class="pump-photo" role="img" aria-label="Two blue submersible pumps" style="background:linear-gradient(135deg,#f4f6f8,#2f8fb0 50%,#eef1f3)"></div><div class="pump-label">CENTRIFUGAL DEWATERING</div></div>
<div class="abs pump-card" style="left:117px;top:2150px"><div class="pump-photo" role="img" aria-label="Red wellpoint pump unit" style="background:linear-gradient(135deg,#f3eeee,#b3242a 50%,#eee9e9)"></div><div class="pump-label">WELLPOINT PUMP</div></div>
<div class="abs pump-card" style="left:446px;top:2150px"><div class="pump-photo" role="img" aria-label="Red enclosed pump on trailer" style="background:linear-gradient(135deg,#f5f5f5,#c0262a 50%,#2c2c2c 80%,#f0f0f0)"></div><div class="pump-label">CENTRIFUGAL DEWATERING</div></div>
<div class="abs pump-card" style="left:775px;top:2150px"><div class="pump-photo" role="img" aria-label="Blue electric centrifugal pump" style="background:linear-gradient(135deg,#f5f7fa,#2f6fb0 50%,#eef2f6)"></div><div class="pump-label">CENTRIFUGAL DEWATERING</div></div>
<div class="abs pump-cta">
  <span class="call">CALL US: 555 210 4471 OR</span>
  <span class="btn">MAKE ENQUIRY</span>
</div>

<section class="abs construction" aria-label="Construction dewatering">
  <h2 class="abs section-title">CONSTRUCTION DEWATERING</h2>
  <div class="abs system" style="left:117px">
    <div class="system-photo" role="img" aria-label="Drilling rigs in an open excavation" style="background:linear-gradient(180deg,#8fa6b8,#6b6a5c 60%,#4f4a3e)"></div>
    <div class="system-label">DEEP WELL SYSTEM</div>
    <p>The Deep Well System is also a versatile predrainage dewatering system which can pump high and low volumes of groundwater. This method is best suited to homogeneous aquifers that extend well below the bottom of the excavation.</p>
  </div>
  <div class="abs system" style="left:446px">
    <div class="system-photo" role="img" aria-label="Workers installing wellpoints in a trench" style="background:linear-gradient(180deg,#c46a3a,#8a7a5e 55%,#5a5246)"></div>
    <div class="system-label">WELL POINT SYSTEM</div>
    <p>The Well Point System is one of the most versatile of pre-drainage methods which can pump a few gallons per minute in fine sandy silts or many thousands of gallons per minute in coarse sands and gravels.</p>
  </div>
  <div class="abs system" style="left:775px">
    <div class="system-photo" role="img" aria-label="Worker connecting blue eductor pipework" style="background:linear-gradient(180deg,#9a7a4e,#2f6fc0 55%,#7b6a4a)"></div>
    <div class="system-label">EDUCTOR SYSTEM</div>
    <p>As many as 100 eductor wells are commonly activated by a single pumping station although this varies considerably on the volumes of water to be pumped and the lift required.</p>
  </div>
</section>

<footer class="abs footer"></footer>
<div class="abs footer-name">Quorvantelline LLC</div>
<div class="abs footer-address">1840 Marrow Lane&nbsp; Coral Bay, Florida, 33099</div>
<div class="abs footer-contact">Toll Free: 555 210 4471&nbsp;&nbsp; | &nbsp;&nbsp;Fax: 555 210 4472&nbsp;&nbsp; | &nbsp;&nbsp;Email: info@quorvantelline.com</div>
<div class="abs badge-a"></div>
<div class="abs badge-b"></div>
<div class="abs footer-rule"></div>
<div class="abs footer-copy">© 2018 Quorvantelline LLC&nbsp; All Rights Reserved</div>
<div class="abs footer-links">Privacy Policy &nbsp;|&nbsp; Site Map &nbsp;|&nbsp; Terms of Service</div>

</body>
</html>
```